Holiday Let Property Management Service and Website. We manage properties for holiday letting

We want a stylish business card that reflects our brand.
*** UPDATE *** PLEASE USE THE RECTANGULAR ORANGE COLOUR SWIPE PROVIDED IN THE DROP BOX FOR THE BSINESS CARD COLOUR.***
Please view the site: www.lodgewell.com.au
Obviously, we want to use the same logo font from our site for the card design.
We want to have the name "Lodgewell" right across the front in white and an orange background colour that matches the orange on our website or a brighter fresher looking orange .
We'd like to have the details on the back similar to what I've shown below but obviously with some more aesthetic added and better positioning than I have provided.
Same colours as the front. white writing and orange background. Once we have the design we'd like the font to be raised and the finish to be a low sheen. Quality thickness and finishes.
---------------------------------------------------------------------------
(Rough idea of writing details on back of card but open to nicer repositioning)

LODGEWELL
Holiday Let Management & Consulting Specialists

Marta Van Kerr Owen Brisk
Principal Director
0492637058 0487350216

email: enquiries@lodgewell.com.au
www.lodgewell.com.au

--------------------------------------------------------------------------

Target Market(s)

Property owners who may want to convert to holiday letting and people seeking holiday accommodation.

Industry/Entity Type

Tourism

Contact Information for Business Card

(Front of card) To have "Lodgewell" to stretch across the card in white writing the same font as our website home page. (discreetly including the logo TM if possible)

------------------------------------------------------------------------------------------------
(Back of card)

LODGEWELL
Holiday Let Consultants & Management Specialists

Marta Van Kerr Owen Brisk
Principal Director
0492637058 0487350216

www.lodgewell.com.au

-----------------------------------------------------------------------------------------------

Font styles to use
Other font styles liked:
• something similar or complimentary to our logo font please

Requirements
Must have
• The same font for our logo name and close to the same colour orange as the orange footer on our website. (if you can make it pop more without going too far away from it that would be great.)
• Orange background front and back with white font.
• *** UPDATE *** PLEASE USE THE RECTANGULAR ORANGE COLOUR SWIPE PROVIDED IN THE DROP BOX FOR THE BSINESS CARD COLOUR.***
Nice to have
• Great symmetry and aesthetics
Should not have
• Any other writing except our brand name (Lodgewell) on the front of the card and a small, discreet trade mark (TM)

```html
<!DOCTYPE html>
<html lang="en">
<head>
<meta charset="utf-8">
<title>Lodgewell Business Card</title>
<link rel="stylesheet" href="https://fonts.googleapis.com/css2?family=Montserrat:wght@400;500;700&display=swap">
<style>
  :root {
    --card-orange: #ff5500;
    --ink-white: #ffffff;
    --table-grey: #3b3b3b;
  }
  * { box-sizing: border-box; margin: 0; padding: 0; }
  html, body {
    width: 1200px; height: 800px; overflow: hidden;
    background: var(--table-grey);
    font-family: "Montserrat", sans-serif;
    color: var(--ink-white);
  }
  .sheet {
    width: 1200px; height: 800px;
    display: flex; align-items: center; justify-content: center; gap: 40px;
  }
  .card {
    width: 540px; height: 309px;
    background: var(--card-orange);
    position: relative;
  }
  .card-front {
    display: flex; align-items: center; justify-content: center;
  }
  .brand-name {
    font-weight: 700;
    font-size: 86px;
    letter-spacing: -2px;
    line-height: 1;
  }
  .card-back { padding: 40px 44px 34px; display: flex; flex-direction: column; }
  .back-brand { align-self: flex-start; text-align: right; }
  .back-brand .brand-name { font-size: 58px; letter-spacing: -1.5px; }
  .tagline { font-size: 11px; font-weight: 500; margin-top: 4px; letter-spacing: 0.2px; }
  .people { display: flex; justify-content: space-between; margin-top: 34px; padding: 0 10px; }
  .person-name { font-size: 20px; font-weight: 400; }
  .person-role { font-size: 11px; letter-spacing: 1.2px; margin-top: 2px; }
  .contact { display: flex; align-items: center; gap: 6px; font-size: 12px; margin-top: 6px; letter-spacing: 0.3px; }
  .contact svg { width: 12px; height: 12px; flex: none; }
  .divider { height: 1px; background: var(--ink-white); margin: 14px 0 10px; }
  .contacts-row { display: flex; justify-content: space-between; padding: 0 10px; }
  .contacts-row .contact { margin-top: 0; }
</style>
</head>
<body>
<main class="sheet">
  <section class="card card-front" aria-label="Card front">
    <h1 class="brand-name">Lodgewell</h1>
  </section>

  <section class="card card-back" aria-label="Card back">
    <div class="back-brand">
      <h2 class="brand-name">Lodgewell</h2>
      <p class="tagline">Holiday Let Consultants &amp; Management Specialists</p>
    </div>

    <div class="people">
      <div class="person">
        <p class="person-name">Marta Van Kerr</p>
        <p class="person-role">PRINCIPAL</p>
        <p class="contact">
          <svg viewBox="0 0 12 12" aria-hidden="true"><rect x="3" y="0.5" width="6" height="11" rx="1.2" fill="none" stroke="#fff"/><circle cx="6" cy="9.3" r="0.8" fill="#fff"/></svg>
          0492637058
        </p>
      </div>
      <div class="person">
        <p class="person-name">Owen Brisk</p>
        <p class="person-role">DIRECTOR</p>
        <p class="contact">
          <svg viewBox="0 0 12 12" aria-hidden="true"><rect x="3" y="0.5" width="6" height="11" rx="1.2" fill="none" stroke="#fff"/><circle cx="6" cy="9.3" r="0.8" fill="#fff"/></svg>
          0487350216
        </p>
      </div>
    </div>

    <div class="divider"></div>

    <div class="contacts-row">
      <p class="contact">
        <svg viewBox="0 0 12 12" aria-hidden="true"><rect x="0.5" y="2.5" width="11" height="7" fill="#fff"/><path d="M0.5 2.5 L6 6.8 L11.5 2.5" fill="none" stroke="#ff5500" stroke-width="1"/></svg>
        enquiries@lodgewell.com.au
      </p>
      <p class="contact">
        <svg viewBox="0 0 12 12" aria-hidden="true"><circle cx="6" cy="6" r="5.3" fill="none" stroke="#fff"/><ellipse cx="6" cy="6" rx="2.3" ry="5.3" fill="none" stroke="#fff"/><line x1="0.7" y1="6" x2="11.3" y2="6" stroke="#fff"/></svg>
        www.lodgewell.com.au
      </p>
    </div>
  </section>
</main>
</body>
</html>
```